MCP phase 1 web design

Meridale Capital Partners Ltd (MCP) is a challenger business to the traditional leasing market. We look for solutions to complex problems involving the funding of capital equipment within an office environment and then build documentation around the solution. We recently created a brief for a logo and successfully completed that assignment. We now need to create our first web site which is simply intended to be informative. To help interested designers we have attached a detailed brief that is broken into three sections. The first explains how we see the site developing over time from something quite straightforward initially to a full transaction capability. Whoever wins this competition will be expected to work with us into the future to help develop the site. Section 2 gives you a view about our likes and dislikes by reviewing some existing sites. Section 3 gives you the structure and content of the site based upon our likes and dislikes. We are by no means committed to the structure and if you believe it can be presented in a better way then please use your design. The text is fixed as content. The images to appear can be anything from photographs to line drawings again entirely at the designers whim. Currently we have a home page plus 5 subsidiary pages. A few things to help you:
1. The logo is fixed and should be amongst the downloads.
2. The colours we have are corporate and should be used.
3. The typeface we use within the business is "Verdana"
Good luck.

```html
<!DOCTYPE html>
<html lang="en">
<head>
<meta charset="utf-8">
<title>Meridale Capital Partners Ltd — Home</title>
<link rel="stylesheet" href="https://fonts.googleapis.com/css2?family=Open+Sans:wght@400;600;700&family=Ubuntu:wght@300;400;500;700&display=swap">
<style>
:root{
  --blue:#4a90cc;
  --blue-dark:#2a6db5;
  --ink:#444444;
  --ink-soft:#666666;
  --muted:#9a9a9a;
  --page:#ffffff;
  --section:#f7f7f7;
  --strip:#f1f1f1;
  --footer:#3d3d3d;
  --footer-rule:#4f4f4f;
  --footer-text:#c8c8c8;
  --accent:#e8642c;
  --client:#cfcfcf;
}
*{box-sizing:border-box;margin:0;padding:0}
html,body{width:1000px;height:1200px;overflow:hidden;background:var(--page)}
body{position:relative;font-family:"Ubuntu",Verdana,sans-serif;color:var(--ink)}
.abs{position:absolute}

/* header */
.brand{left:96px;top:26px;display:flex;align-items:center;gap:9px}
.brand-mark{width:22px;height:22px;background:var(--blue-dark)}
.brand-name{font-family:"Open Sans",sans-serif;font-weight:400;color:var(--blue-dark);font-size:17px;line-height:14px;letter-spacing:.5px;text-transform:uppercase}
.brand-name small{display:block;font-size:8.5px;letter-spacing:1.6px}
.main-nav{top:31px;left:0;width:1000px;font-family:Arial,Helvetica,sans-serif;font-size:10.5px;font-weight:700;color:#333}
.main-nav span{position:absolute;white-space:nowrap}
.main-nav .active{color:var(--blue-dark)}
.nav-caret{left:803px;top:40px;font-family:Arial,sans-serif;font-size:8px;color:#555}
.nav-indicator{left:596px;top:72px;width:37px;height:3px;background:var(--blue-dark)}
.nav-indicator::after{content:"";position:absolute;left:14px;top:-4px;border:4px solid transparent;border-top:0;border-bottom:4px solid var(--blue-dark)}

/* hero */
.hero-band{left:36px;top:75px;width:927px;height:332px;background:linear-gradient(180deg,#e6e6e6,#efefef);box-shadow:inset 0 2px 3px rgba(0,0,0,.08)}
.hero-card{left:90px;top:94px;width:821px;height:297px;background:#fff}
.hero-photo{left:495px;top:94px;width:388px;height:297px;background:linear-gradient(135deg,#f4f1ee 0%,#e9eef6 55%,#dbe6f3 100%)}
.hero-copy{left:143px;top:143px;width:340px;font-family:"Open Sans",sans-serif}
.hero-kicker{color:var(--blue);font-size:20px;font-weight:700;line-height:24px}
.hero-title{color:var(--ink);font-size:33px;font-weight:700;line-height:31px;margin-top:1px}
.hero-sub{color:var(--ink);font-size:23.5px;font-weight:400;line-height:23px;text-transform:uppercase}
.hero-text{color:var(--muted);font-size:8.4px;line-height:12.5px;margin-top:5px;text-transform:uppercase;width:326px}
.hero-button{left:143px;top:296px;width:106px;height:28px;background:var(--blue);color:#fff;font-family:"Open Sans",sans-serif;font-size:10px;font-weight:600;display:flex;align-items:center;justify-content:center}
.hero-arrows{left:141px;top:340px;font-family:Arial,sans-serif;font-size:19px;font-weight:700;color:#333;letter-spacing:8px}

/* services */
.section-bg{left:36px;top:407px;width:927px;height:520px;background:var(--section)}
.service{width:270px}
.service-icon{position:absolute;left:0;top:0}
.service-title{position:absolute;left:64px;top:-1px;font-size:15.5px;font-weight:500;line-height:18px;color:var(--ink);text-transform:uppercase;letter-spacing:.2px;white-space:nowrap}
.service-text{position:absolute;left:65px;top:52px;width:210px;font-size:9px;line-height:15.5px;color:var(--ink-soft)}
.btn-more{position:absolute;left:1px;top:115px;width:60px;height:30px;background:linear-gradient(#4a4a4a,#333);border-radius:2px;color:#fff;font-size:10.5px;display:flex;align-items:center;justify-content:center}

/* why choose us */
.why-box{left:90px;top:640px;width:400px;height:248px;background:#efefef;border:1px solid #e2e2e2;border-radius:2px}
.why-photo{left:100px;top:655px;width:142px;height:232px;background:linear-gradient(180deg,#e9e4df 0%,#7a6a60 45%,#2a2a2a 100%)}
.why-title{left:262px;top:663px;font-size:18px;font-weight:400;color:var(--ink)}
.why-lead{left:262px;top:696px;width:215px;font-size:10px;line-height:17px;color:var(--ink)}
.why-list{left:262px;top:736px;width:162px;list-style:none}
.why-list li{position:relative;padding-left:14px;height:35px;line-height:21px;font-size:9.2px;color:var(--ink);border-bottom:1px solid #dcdcdc;white-space:nowrap}
.why-list li:last-child{border-bottom:0}
.why-list li::before{content:"";position:absolute;left:0;top:7px;width:7px;height:7px;border-radius:50%;background:var(--accent)}

/* video */
.video-title{left:581px;top:639px;font-size:16px;font-weight:300;color:#333;letter-spacing:-.3px}
.video-rule{left:581px;top:675px;width:329px;height:1px;background:#cfcfcf}
.video-frame{left:581px;top:698px;width:329px;height:180px;background:#fff;border:1px solid #d6d6d6;box-shadow:inset 0 0 0 3px #fff,inset 0 0 0 4px #e4e4e4}
.video-play{left:720px;top:756px}

/* clients */
.clients-strip{left:36px;top:927px;width:927px;height:75px;background:var(--strip);border-top:1px solid #e4e4e4}
.clients-label{left:90px;top:948px;font-size:12.5px;font-weight:700;line-height:14px;color:#333}
.client{font-family:"Ubuntu",sans-serif;font-weight:700;color:var(--client);white-space:nowrap;line-height:1}

/* footer */
.site-footer{left:36px;top:1002px;width:927px;height:198px;background:var(--footer)}
.footer-col{top:1028px;height:162px;border-right:1px solid var(--footer-rule)}
.footer-col h4{position:absolute;left:0;top:8px;font-family:Arial,Helvetica,sans-serif;font-size:9.5px;font-weight:700;color:#fff;text-transform:uppercase}
.footer-col ul{position:absolute;left:0;top:39px;list-style:none}
.footer-col li{font-family:Arial,Helvetica,sans-serif;font-size:7.4px;height:21px;color:var(--footer-text);text-transform:uppercase;white-space:nowrap}
.footer-col li::before{content:"›";margin-right:5px;font-size:9px}
.footer-col li.current{color:var(--blue)}
.footer-contact{font-family:Arial,Helvetica,sans-serif;font-size:8.6px;line-height:12px;color:var(--footer-text)}
.footer-brand{left:723px;top:1113px;font-family:"Open Sans",sans-serif;font-size:9px;line-height:8px;color:#fff;text-transform:uppercase;letter-spacing:.4px}
.footer-brand small{display:block;font-size:5px;letter-spacing:.8px;margin-top:2px}
.footer-legal{left:826px;top:1112px;font-family:Arial,sans-serif;font-size:7.5px;line-height:10px;color:#fff;font-weight:700}
.footer-legal span{color:var(--blue);font-weight:400}
.social{top:1152px;width:26px;height:26px;border-radius:50%;background:#8a8a8a}
.to-top{left:917px;top:1157px;width:30px;height:30px}
</style>
</head>
<body>

<header>
  <div class="abs brand">
    <span class="brand-mark" aria-hidden="true"></span>
    <span class="brand-name">Meridale<small>Capital Partners Ltd</small></span>
  </div>
  <nav class="abs main-nav">
    <span class="active" style="left:600px">HOME</span>
    <span style="left:657px">WHY MERIDALE</span>
    <span style="left:778px">SOLUTIONS</span>
    <span style="left:857px">CONTACT</span>
  </nav>
  <span class="abs nav-caret">&#711;</span>
  <span class="abs nav-indicator"></span>
</header>

<section class="hero">
  <div class="abs hero-band"></div>
  <div class="abs hero-card"></div>
  <div class="abs hero-photo" role="img" aria-label="Photograph of a smiling woman holding a fan of banknotes and a piggy bank"></div>
  <div class="abs hero-copy">
    <p class="hero-kicker">WELCOME!</p>
    <h1 class="hero-title">ACHIEVE</h1>
    <p class="hero-sub">Your goals and<br>long-term success</p>
    <p class="hero-text">We provide "sales aid finance" through Meridale financial and contract solutions. Specialising in the print and technology markets, we offer value added resellers (VARs)</p>
  </div>
  <a class="abs hero-button">READ MORE</a>
  <div class="abs hero-arrows">‹›</div>
</section>

<main>
  <div class="abs section-bg"></div>

  <article class="abs service" style="left:90px;top:447px">
    <svg class="service-icon" width="50" height="46" viewBox="0 0 50 46" aria-hidden="true"><polygon points="12,1 38,1 50,23 38,45 12,45 0,23" fill="#4a4a4a"/><circle cx="25" cy="17" r="6" fill="#fff"/><path d="M15 34c1-7 5-9 10-9s9 2 10 9z" fill="#fff"/></svg>
    <h2 class="service-title">Managed Services<br>Solutions</h2>
    <p class="service-text">MCP's Managed Services solutions offer all the flexibility required by a technology project, within the framework of a robust, transpar-</p>
    <a class="btn-more">More</a>
  </article>

  <article class="abs service" style="left:371px;top:447px">
    <svg class="service-icon" width="50" height="46" viewBox="0 0 50 46" aria-hidden="true"><polygon points="12,1 38,1 50,23 38,45 12,45 0,23" fill="#4a4a4a"/><path d="M12 22l6-5 7 3 7-3 6 5-9 8-4-2-4 2z" fill="#fff"/></svg>
    <h2 class="service-title">Public Sector<br>Solutions</h2>
    <p class="service-text">MCP's Managed Services solutions offer all the flexibility required by a technology project, within the framework of a robust, transpar-</p>
    <a class="btn-more">More</a>
  </article>

  <article class="abs service" style="left:652px;top:447px">
    <svg class="service-icon" width="50" height="46" viewBox="0 0 50 46" aria-hidden="true"><polygon points="12,1 38,1 50,23 38,45 12,45 0,23" fill="#4a4a4a"/><path d="M10 20l15-6 15 6-15 6z M17 24v6c3 3 13 3 16 0v-6l-8 3z" fill="#fff"/></svg>
    <h2 class="service-title">Education<br>Solutions</h2>
    <p class="service-text">MCP's Managed Services solutions offer all the flexibility required by a technology project, within the framework of a robust, transpar-</p>
    <a class="btn-more">More</a>
  </article>

  <section>
    <div class="abs why-box"></div>
    <div class="abs why-photo" role="img" aria-label="Photograph of a businesswoman in a dark jacket"></div>
    <h2 class="abs why-title">Why Choose Us?</h2>
    <p class="abs why-lead">Lorem ipsum dolor sit amet, consectetur adipisicing elit, sed do eiusmod tempor.</p>
    <ul class="abs why-list">
      <li>Sed ut perspiciatis unde omnis iste</li>
      <li>Accusantium doloremque laudant</li>
      <li>Rotam rem aperiam eaque ipsa uae</li>
      <li>Aillo inventore veritatis et quasi</li>
    </ul>
  </section>

  <section>
    <h2 class="abs video-title">Latest Video</h2>
    <div class="abs video-rule"></div>
    <div class="abs video-frame"></div>
    <svg class="abs video-play" width="52" height="52" viewBox="0 0 52 52" aria-hidden="true"><circle cx="26" cy="26" r="24" fill="#e6e6e6" stroke="#cfcfcf" stroke-width="2"/><circle cx="26" cy="26" r="20" fill="#f3f3f3"/><path d="M20 14l17 12-17 12z" fill="#b5b5b5"/></svg>
  </section>
</main>

<section>
  <div class="abs clients-strip"></div>
  <p class="abs clients-label">Our most<br>recent clients</p>
  <span class="abs client" style="left:232px;top:949px;font-size:24px">BRIGHTLY</span>
  <span class="abs client" style="left:374px;top:943px;font-size:33px">NORVA</span>
  <span class="abs client" style="left:514px;top:952px;font-size:19px">KESTRAL</span>
  <span class="abs client" style="left:656px;top:952px;font-size:19px">HALVEN</span>
  <span class="abs client" style="left:794px;top:953px;font-size:18px">OAKMERE</span>
</section>

<footer>
  <div class="abs site-footer"></div>
  <div class="abs footer-col" style="left:90px;width:120px">
    <h4>Company</h4>
    <ul><li>About us</li><li>Case studies</li><li>Testimonials</li><li>Why choose us</li></ul>
  </div>
  <div class="abs footer-col" style="left:231px;width:120px">
    <h4>Overview</h4>
    <ul><li>What we do</li><li>Solutions</li></ul>
  </div>
  <div class="abs footer-col" style="left:372px;width:120px">
    <h4>For members</h4>
    <ul><li>Forums</li><li>News</li></ul>
  </div>
  <div class="abs footer-col" style="left:513px;width:120px">
    <h4>Navigation</h4>
    <ul><li class="current">Home</li><li>Why Meridale</li><li>Solutions</li><li>Contact</li></ul>
  </div>

  <svg class="abs" style="left:723px;top:1036px" width="13" height="12" viewBox="0 0 13 12" aria-hidden="true"><path d="M6.5 0L13 6h-2v6H8V8H5v4H2V6H0z" fill="#fff"/></svg>
  <p class="abs footer-contact" style="left:745px;top:1034px">412 Harbour Row,<br>Kelmouth, KM 12 7QD.</p>
  <svg class="abs" style="left:722px;top:1073px" width="14" height="15" viewBox="0 0 14 15" aria-hidden="true"><rect width="14" height="15" rx="2" fill="#fff"/><path d="M4 3c-1 2 0 6 4 9l2-2-2-2-1 1c-1-1-2-3-2-4l1-1z" fill="#3d3d3d"/></svg>
  <p class="abs footer-contact" style="left:748px;top:1073px">Telephone: +1 800 555 0142<br>FAX: +1 800 555 0187</p>

  <p class="abs footer-brand">MCP Meridale<small>Capital Partners Ltd</small></p>
  <p class="abs footer-legal"><span>© 2014</span><br>PRIVACY POLICY</p>

  <span class="abs social" style="left:724px"></span>
  <span class="abs social" style="left:752px"></span>
  <svg class="abs" style="left:780px;top:1152px" width="26" height="26" viewBox="0 0 26 26" aria-hidden="true"><circle cx="13" cy="13" r="13" fill="#8a8a8a"/><rect x="7" y="8.5" width="12" height="9" fill="#fff"/><path d="M7 8.5l6 5 6-5" fill="none" stroke="#8a8a8a" stroke-width="1.3"/></svg>
  <span class="abs social" style="left:808px"></span>

  <svg class="abs to-top" viewBox="0 0 30 30" aria-hidden="true"><circle cx="15" cy="15" r="15" fill="#fff"/><path d="M8 18l7-7 7 7" fill="none" stroke="#333" stroke-width="3"/></svg>
</footer>

</body>
</html>
```